Crestwell Renewal Business Card Design Phase 2

Professional and clean design. The design colors should flow with the logo. Two-sided card with the website on the back which is:

www.CrestwellRenewal.example.

"Specializing in Water Damage Restoration"

On the front I need the name, email, phone, and logo.

Name: Dorian Halvek
Email: Dorian@CrestwellRenewal.example
Phone: 555-318-2046 for now

I only have the Preview and Thumbnail right now but should have the source files uploaded within a day or two.

Target Market(s)

Flood victims, home owners with water damage from busted pipes etc...

Industry/Entity Type

Business

Contact Information for Business Card

Name: Dorian Halvek

Font styles to use
Serif
Sans Serif

Requirements
Must have
• Business Card Details Info

```html
<!DOCTYPE html>
<html lang="en">
<head>
<meta charset="utf-8">
<title>Crestwell Renewal Business Card</title>
<link rel="stylesheet" href="https://fonts.googleapis.com/css2?family=Cinzel:wght@500&family=Open+Sans:wght@400;600;800&display=swap">
<style>
  :root {
    --page-bg: #e9e9e6;
    --card-bg: #ffffff;
    --brand-blue: #1f4585;
    --brand-green: #5aab47;
    --ink-blue: #1d3f7a;
    --white: #ffffff;
  }
  * { box-sizing: border-box; margin: 0; padding: 0; }
  html, body { width: 1200px; height: 780px; overflow: hidden; }
  body {
    background: var(--page-bg);
    display: flex;
    align-items: center;
    justify-content: center;
    gap: 40px;
    font-family: "Open Sans", Arial, sans-serif;
  }
  .card {
    position: relative;
    width: 560px;
    height: 320px;
    background: var(--card-bg);
    box-shadow: 0 6px 18px rgba(0,0,0,0.18);
    overflow: hidden;
  }
  .card__wave { position: absolute; inset: 0; width: 100%; height: 100%; }
  .card__name {
    position: absolute; left: 34px; top: 48px;
    font-family: "Cinzel", Georgia, serif;
    font-weight: 500; font-size: 22px; letter-spacing: 1.5px;
    color: var(--ink-blue);
  }
  .brand {
    position: absolute; text-align: center;
  }
  .brand__name {
    font-family: "Open Sans", Arial, sans-serif;
    font-weight: 800; text-transform: uppercase;
    color: var(--brand-blue); line-height: 1.05; letter-spacing: 0.5px;
  }
  .brand__tagline {
    margin-top: 6px;
    font-size: 11.5px; color: var(--brand-green); letter-spacing: 0.3px;
    white-space: nowrap;
  }
  .card--front .brand { right: 28px; top: 22px; width: 260px; }
  .card--front .brand__name { font-size: 28px; }
  .card--back .brand { left: 0; right: 60px; top: 48px; }
  .card--back .brand__name { font-size: 40px; }
  .contact {
    position: absolute; left: 34px; top: 186px;
    list-style: none; font-size: 13px; color: var(--ink-blue);
  }
  .contact__item { display: flex; align-items: center; gap: 8px; margin-bottom: 5px; }
  .contact__icon { width: 14px; height: 14px; }
  .card__web {
    position: absolute; right: 26px; bottom: 22px;
    font-size: 14px; font-weight: 600; color: var(--white); letter-spacing: 0.3px;
  }
</style>
</head>
<body>

<section class="card card--front" aria-label="Card front">
  <svg class="card__wave" viewBox="0 0 560 320" aria-hidden="true">
    <path fill="var(--brand-green)" d="M0,272 C180,272 320,250 410,195 C460,164 510,140 560,132 L560,144 C512,152 466,176 420,206 C330,262 190,290 0,290 Z"/>
    <path fill="var(--brand-blue)" d="M0,300 C190,300 340,276 432,220 C480,190 520,168 560,162 L560,320 L0,320 Z"/>
  </svg>
  <h1 class="card__name">Dorian Halvek</h1>
  <div class="brand">
    <p class="brand__name">Crestwell<br>Renewal</p>
    <p class="brand__tagline">Specializing in Water Damage Restoration</p>
  </div>
  <ul class="contact">
    <li class="contact__item">
      <svg class="contact__icon" viewBox="0 0 14 14" aria-hidden="true"><rect width="14" height="14" fill="var(--brand-green)"/><path d="M4 3 L6 3 L6.5 5.5 L5.3 6.3 Q6.2 8 7.7 8.7 L8.5 7.5 L11 8 L11 10 Q7 11 4 7 Q3 5 4 3 Z" fill="var(--white)"/></svg>
      <span>555-318-2046</span>
    </li>
    <li class="contact__item">
      <svg class="contact__icon" viewBox="0 0 14 14" aria-hidden="true"><rect width="14" height="14" fill="var(--brand-green)"/><rect x="3" y="4" width="8" height="6" fill="none" stroke="var(--white)" stroke-width="1"/><path d="M3 4 L7 7.5 L11 4" fill="none" stroke="var(--white)" stroke-width="1"/></svg>
      <span>Dorian@CrestwellRenewal.example</span>
    </li>
  </ul>
  <p class="card__web">www.CrestwellRenewal.example</p>
</section>

<section class="card card--back" aria-label="Card back">
  <svg class="card__wave" viewBox="0 0 560 320" aria-hidden="true">
    <path fill="var(--brand-green)" d="M0,272 C180,272 320,250 410,195 C460,164 510,140 560,132 L560,144 C512,152 466,176 420,206 C330,262 190,290 0,290 Z"/>
    <path fill="var(--brand-blue)" d="M0,300 C190,300 340,276 432,220 C480,190 520,168 560,162 L560,320 L0,320 Z"/>
  </svg>
  <div class="brand">
    <p class="brand__name">Crestwell<br>Renewal</p>
    <p class="brand__tagline">Specializing in Water Damage Restoration</p>
  </div>
  <p class="card__web">www.CrestwellRenewal.example</p>
</section>

</body>
</html>
```